Designer Instructions – Updated Referral Program Flyer

(Based on the mock-up in “Brief Layout and Instructions.pdf”)

OVERALL STYLE + LAYOUT

Maintain the same general layout, structure, and flow as the mock-up flyer (front and back).

This is an update of an older flyer, not a full redesign — keep the same sections, proportions, and overall visual feel, but with cleaner, more modern design improvements.

The final flyer should look clean, bold, professional, and high-impact, geared toward realtors, property managers, and contractors who refer work.

FRONT SIDE INSTRUCTIONS
1. Header Section

Remove the Tallow Ridge Builders logo from the top banner.
(Shown on page 1 of the PDF)

2. Main Headline

Keep the same three-line structure:
EARN
UNLIMITED
CASH

Center it, maximize impact, and increase the font size of CASH so all three words match in importance.

Make the headline bold, clean, and the main focal point.

3. Cash Incentive Box

Keep the "$500 minimum OR 10% per referral" box, but upgrade the graphics to look sharper and more modern.

Ensure the wording matches exactly what’s in the mock-up.

4. Premier Partner Program Ribbon

Clean up and modernize the "PREMIER PARTNER PROGRAM" bar while keeping the same position and structure.

Ensure the checkmark badge remains crisp and professional.

5. Supporting Icons Section

Keep the four icons/benefit boxes (Guaranteed Payout, Free Evaluations, Affordable Solutions, Industry Leaders) in the same order.

Update the icons to cleaner, more modern styles — but maintain the same meanings.

Improve alignment and spacing for sharper visual consistency.

6. Remove Icons in Contact Area

At the bottom (“CALL TEXT OR BOOK ONLINE 555-014-2796 TallowRidgeBuilders.example”), remove the phone and internet icons, as noted on page 2 of the PDF.

7. Replace All Images

I (Darnell) will provide all updated stock images separately via email.

Replace the flood/water-damage imagery and roof leak with the new images I send.

Keep image placement and proportions the same as the mock-up.

BACK SIDE INSTRUCTIONS
1. Header Image + “REFER / EARN” Section

Maintain the same large split-image layout (“The more you refer, the more you earn”).

Replace all background imagery with the new assets I will send.

Keep the CASH FLOW image section but modernize the type and spacing.

2. “HOW IT WORKS” Section

Preserve the three-column layout:

Refer Flood, Water & Mold Damage

We Take Care of Everything (evaluations/insurance)

Get Paid to Share

Update images, tighten spacing, and use modern iconography.

3. Remove Phone/Internet Icons

Same as the front side — remove small communication icons and keep only the text/number/URL.

4. Bottom Contact Bar

Keep the blue bar, same wording, same layout — just modernize the style if needed for clarity.

5. Replace All Back-Side Images

Again, I will email you the image assets.

Keep the layout EXACT — just update with higher-quality photos and improved design.

TEXT CONTENT (Keep as-is unless spacing adjustments needed)

All text shown in the PDF should remain exactly the same unless spacing or visual balance requires minor adjustments.
Example from page 3:

“REFER FLOOD, MOLD & CONSTRUCTION JOBS”

“We Schedule a Free Estimate. If Approved, You Get Paid.”

“Everybody Benefits From Referrals”

Everything stays, just refreshed and visually improved.

DESIGN GOALS

Flyer should look high-end and trustworthy, not salesy.

Consistent color theme: blues, whites, yellows, same palette as original.

Use bold, modern fonts with strong readability.

Ensure all headlines pop and all benefit boxes are clean, well-aligned, and evenly spaced.

The final result should feel like a premium referral program flyer for a top-tier restoration/remodel company.

FILES I WILL PROVIDE

I will send the designer:

All replacement stock photos

Any updated logos (if needed)

Original high-resolution version of the mock-up (if available)

Any additional icons preferred

0054AA
0677BA
7BADD7
CADEEF
E8F1F8

• Designer Instructions – Updated Referral Program Flyer (Based on the mock-up in “Brief Layout and Instructions.pdf”) OVERALL STYLE + LAYOUT Maintain the same general layout, structure, and flow as the mock-up flyer (front and back). This is an update of an older flyer, not a full redesign — keep the same sections, proportions, and overall visual feel, but with cleaner, more modern design improvements. The final flyer should look clean, bold, professional, and high-impact, geared toward realtors, property managers, and contractors who refer work. FRONT SIDE INSTRUCTIONS 1. Header Section Remove the Tallow Ridge Builders logo from the top banner. (Shown on page 1 of the PDF) 2. Main Headline Keep the same three-line structure: EARN UNLIMITED CASH Center it, maximize impact, and increase the font size of CASH so all three words match in importance. Make the headline bold, clean, and the main focal point. 3. Cash Incentive Box Keep the "$500 minimum OR 10% per referral" box, but upgrade the graphics to look sharper and more modern. Ensure the wording matches exactly what’s in the mock-up. 4. Premier Partner Program Ribbon Clean up and modernize the "PREMIER PARTNER PROGRAM" bar while keeping the same position and structure. Ensure the checkmark badge remains crisp and professional. 5. Supporting Icons Section Keep the four icons/benefit boxes (Guaranteed Payout, Free Evaluations, Affordable Solutions, Industry Leaders) in the same order. Update the icons to cleaner, more modern styles — but maintain the same meanings. Improve alignment and spacing for sharper visual consistency. 6. Remove Icons in Contact Area At the bottom (“CALL TEXT OR BOOK ONLINE 555-014-2796 TallowRidgeBuilders.example”), remove the phone and internet icons, as noted on page 2 of the PDF. 7. Replace All Images I (Darnell) will provide all updated stock images separately via email. Replace the flood/water-damage imagery and roof leak with the new images I send. Keep image placement and proportions the same as the mock-up. BACK SIDE INSTRUCTIONS 1. Header Image + “REFER / EARN” Section Maintain the same large split-image layout (“The more you refer, the more you earn”). Replace all background imagery with the new assets I will send. Keep the CASH FLOW image section but modernize the type and spacing. 2. “HOW IT WORKS” Section Preserve the three-column layout: Refer Flood, Water & Mold Damage We Take Care of Everything (evaluations/insurance) Get Paid to Share Update images, tighten spacing, and use modern iconography. 3. Remove Phone/Internet Icons Same as the front side — remove small communication icons and keep only the text/number/URL. 4. Bottom Contact Bar Keep the blue bar, same wording, same layout — just modernize the style if needed for clarity. 5. Replace All Back-Side Images Again, I will email you the image assets. Keep the layout EXACT — just update with higher-quality photos and improved design. TEXT CONTENT (Keep as-is unless spacing adjustments needed) All text shown in the PDF should remain exactly the same unless spacing or visual balance requires minor adjustments. Example from page 3: “REFER FLOOD, MOLD & CONSTRUCTION JOBS” “We Schedule a Free Estimate. If Approved, You Get Paid.” “Everybody Benefits From Referrals” Everything stays, just refreshed and visually improved. DESIGN GOALS Flyer should look high-end and trustworthy, not salesy. Consistent color theme: blues, whites, yellows, same palette as original. Use bold, modern fonts with strong readability. Ensure all headlines pop and all benefit boxes are clean, well-aligned, and evenly spaced. The final result should feel like a premium referral program flyer for a top-tier restoration/remodel company. FILES I WILL PROVIDE I will send the designer: All replacement stock photos Any updated logos (if needed) Original high-resolution version of the mock-up (if available) Any additional icons preferred

```html
<!DOCTYPE html>
<html lang="en">
<head>
<meta charset="utf-8">
<title>Referral Partner Program Flyer – Front and Back</title>
<link href="https://fonts.googleapis.com/css2?family=Montserrat:wght@700;800;900&family=Oswald:wght@500;600;700&family=Bebas+Neue&family=Open+Sans:wght@600;700&display=swap" rel="stylesheet">
<style>
  :root{
    --stage:#c3c3c3;
    --navy:#0b2d6b;
    --navy-deep:#0a2458;
    --royal:#0054aa;
    --yellow:#ffe100;
    --orange:#f7a21b;
    --red:#d7191c;
    --red-dark:#a80f12;
    --hex-gray:#cfd5db;
    --steel:#6f8594;
    --card:#f3f7fc;
    --white:#ffffff;
    --ink:#111111;
  }
  *{box-sizing:border-box;margin:0;padding:0}
  html,body{width:1200px;height:956px;overflow:hidden;background:var(--stage)}
  .canvas{position:relative;width:1200px;height:956px;background:var(--stage)}
  .flyer{position:absolute;top:154px;width:420px;height:649px;background:var(--white);overflow:hidden}
  .flyer--front{left:168px}
  .flyer--back{left:612px}
  .abs{position:absolute}

  /* Front header */
  .front-header{position:absolute;left:0;top:0;width:420px;height:229px;background:var(--white)}
  .front-header__panel{position:absolute;inset:0;background:var(--navy);
    clip-path:polygon(0 0,253px 0,202px 114px,253px 229px,0 229px)}
  .front-header__photo{position:absolute;inset:0;
    background:linear-gradient(160deg,#d9d6cf 0%,#b9b4aa 35%,#5fa6cf 60%,#3f86b7 80%,#8d9197 100%);
    clip-path:polygon(262px 0,420px 0,420px 229px,262px 229px,211px 114px)}
  .headline{position:absolute;left:0;width:212px;text-align:center;font-family:"Montserrat",sans-serif;font-weight:900;line-height:1;letter-spacing:-1px}
  .headline--earn{top:39px;font-size:54px;color:var(--yellow)}
  .headline--unlimited{top:96px;font-size:31px;color:var(--white);letter-spacing:-0.5px}
  .headline--cash{top:128px;font-size:52px;color:var(--yellow)}

  /* Incentive */
  .incentive{position:absolute;left:0;top:229px;width:420px;height:130px}
  .incentive__label{position:absolute;top:100px;font-family:"Montserrat",sans-serif;font-weight:800;font-size:11.5px;color:var(--ink);transform:translateX(-50%);white-space:nowrap}
  .premier{position:absolute;left:235px;top:33px;width:174px}
  .premier__eyebrow{text-align:center;font-family:"Montserrat",sans-serif;font-weight:700;font-size:8.5px;letter-spacing:5px;color:var(--red);padding-left:5px}
  .premier__bar{position:relative;margin-top:4px;height:24px}
  .premier__part{position:absolute;top:0;height:24px;width:74px;font-family:"Montserrat",sans-serif;font-weight:800;font-size:11.5px;color:var(--white);display:flex;align-items:center;justify-content:center}
  .premier__part--red{left:0;background:var(--red)}
  .premier__part--gray{right:0;background:var(--steel)}
  .premier__badge{position:absolute;left:74px;top:-3px;width:26px;height:30px}

  /* Ribbon */
  .ribbon{position:absolute;left:0;top:357px;width:420px;height:64px}
  .ribbon__text{position:absolute;left:57px;width:304px;top:13px;text-align:center;font-family:"Montserrat",sans-serif;font-weight:800;font-size:12.3px;color:var(--white);letter-spacing:0.1px;white-space:nowrap}

  /* Benefits */
  .benefit{position:absolute;top:448px;width:91px;height:96px;background:var(--card);border-radius:6px;box-shadow:0 1px 3px rgba(10,36,88,.18);text-align:center}
  .benefit__icon{position:absolute;left:27px;top:-20px;width:37px;height:37px;border-radius:50%;background:var(--navy);box-shadow:0 0 0 2px var(--white);display:flex;align-items:center;justify-content:center}
  .benefit__title{position:absolute;left:0;right:0;top:29px;font-family:"Montserrat",sans-serif;font-weight:800;font-size:8.6px;line-height:10.5px;color:var(--navy)}
  .benefit__body{position:absolute;left:4px;right:4px;top:55px;font-family:"Open Sans",sans-serif;font-weight:700;font-size:6.3px;line-height:9.3px;color:var(--ink)}
  .hl{color:var(--red)}

  /* Bottom bands */
  .band-red{position:absolute;left:0;top:554px;width:420px;height:45px;background:var(--red);display:flex;align-items:center;justify-content:center;font-family:"Oswald",sans-serif;font-weight:600;font-size:20px;color:var(--white);white-space:nowrap;letter-spacing:-0.3px}
  .band-red .y{color:var(--yellow)}
  .band-blue{position:absolute;left:0;top:599px;width:420px;height:50px;background:var(--navy);display:flex;align-items:center;justify-content:center;gap:4px;font-family:"Oswald",sans-serif;font-weight:500;color:var(--white);white-space:nowrap;letter-spacing:-0.2px}
  .band-blue__call{font-size:13px}
  .band-blue__phone{font-size:17px;font-weight:600;color:var(--yellow)}
  .band-blue__web{font-size:12px}

  /* Back header */
  .back-header{position:absolute;left:0;top:0;width:420px;height:229px}
  .back-header__panel{position:absolute;inset:0;background:linear-gradient(160deg,var(--royal) 0%,var(--navy) 45%,var(--navy-deep) 100%);
    clip-path:polygon(0 0,174px 0,225px 229px,0 229px)}
  .back-header__photo{position:absolute;inset:0;background:linear-gradient(135deg,#dfe3d6 0%,#b9c2ae 40%,#cfd3c4 70%,#9aa48f 100%);
    clip-path:polygon(178px 0,420px 0,420px 229px,229px 229px)}
  .slogan{position:absolute;left:22px;width:147px;text-align:center;font-family:"Bebas Neue",sans-serif;line-height:1;color:var(--white)}
  .slogan--small{font-size:32px}
  .slogan--big{font-size:74px;letter-spacing:-0.5px;background:linear-gradient(180deg,var(--yellow) 0%,var(--orange) 100%);-webkit-background-clip:text;background-clip:text;color:transparent}

  /* How it works */
  .how{position:absolute;left:0;top:229px;width:313px;height:43px;background:var(--yellow);clip-path:polygon(0 0,278px 0,313px 43px,0 43px)}
  .how__title{position:absolute;left:29px;top:234px;font-family:"Montserrat",sans-serif;font-weight:900;font-size:26.5px;line-height:1.2;color:var(--navy);letter-spacing:-0.3px}
  .step{position:absolute;top:292px;width:127px;height:238px;background:var(--card);border-radius:8px;box-shadow:0 1px 3px rgba(10,36,88,.18);text-align:center}
  .step__image{position:absolute;left:3px;top:3px;width:121px;height:124px;border-radius:8px}
  .step__image--city{background:linear-gradient(180deg,#8a7fc4 0%,#b08fb4 40%,#c48a62 60%,#3f3f78 75%,#5a5794 100%)}
  .step__image--home{background:linear-gradient(160deg,#e7ecef 0%,#9bb6c9 40%,#4f87bb 70%,#e8eef3 100%)}
  .step__image--sign{background:linear-gradient(160deg,#b4cfe8 0%,#e9f0f7 40%,#f0d81f 60%,#e9d21a 75%,#9cc1e0 100%)}
  .step__title{position:absolute;left:4px;right:4px;top:142px;font-family:"Montserrat",sans-serif;font-weight:800;font-size:9.4px;line-height:11.6px;color:var(--navy)}
  .step__body{position:absolute;left:6px;right:6px;font-family:"Open Sans",sans-serif;font-weight:700;font-size:8px;line-height:11.4px;color:var(--ink)}
</style>
</head>
<body>
<div class="canvas">

  <!-- FRONT SIDE -->
  <section class="flyer flyer--front">
    <div class="front-header">
      <div class="front-header__panel"></div>
      <div class="front-header__photo" role="img" aria-label="Water damage restoration photo: blue dehumidifier and air mover running in a basement room"></div>
      <div class="headline headline--earn">EARN</div>
      <div class="headline headline--unlimited">UNLIMITED</div>
      <div class="headline headline--cash">CASH</div>
    </div>

    <div class="incentive">
      <svg class="abs" style="left:0;top:0" width="240" height="100" viewBox="0 0 240 100">
        <polygon points="55,10 94,32.5 94,77.5 55,100 16,77.5 16,32.5" fill="var(--hex-gray)"/>
        <circle cx="55" cy="55" r="31" fill="var(--red)"/>
        <text x="55" y="63.5" text-anchor="middle" font-family="Oswald, sans-serif" font-weight="600" font-size="24" fill="#fff">$500</text>
        <circle cx="117" cy="55" r="14" fill="var(--yellow)"/>
        <text x="117" y="62" text-anchor="middle" font-family="Oswald, sans-serif" font-weight="700" font-size="19" fill="var(--navy)">OR</text>
        <polygon points="179,10 218,32.5 218,77.5 179,100 140,77.5 140,32.5" fill="var(--hex-gray)"/>
        <circle cx="179" cy="55" r="31" fill="var(--red)"/>
        <text x="179" y="65" text-anchor="middle" font-family="Oswald, sans-serif" font-weight="500" font-size="29" fill="#fff">10%</text>
      </svg>
      <div class="incentive__label" style="left:55px">Minimum</div>
      <div class="incentive__label" style="left:179px">PER REFERRAL!</div>

      <div class="premier">
        <div class="premier__eyebrow">PREMIER</div>
        <div class="premier__bar">
          <div class="premier__part premier__part--red">PARTNER</div>
          <svg class="premier__badge" viewBox="0 0 26 30">
            <path d="M13 1 L24 5 L24 14 C24 21 19 26 13 29 C7 26 2 21 2 14 L2 5 Z" fill="#c9a13b"/>
            <path d="M13 4 L21 7 L21 14 C21 19 17.5 23 13 25.5 C8.5 23 5 19 5 14 L5 7 Z" fill="#e8c766"/>
            <path d="M8 14.5 L11.8 18.5 L18.5 10" fill="none" stroke="#fff" stroke-width="2.6" stroke-linecap="round" stroke-linejoin="round"/>
          </svg>
          <div class="premier__part premier__part--gray">PROGRAM</div>
        </div>
      </div>
    </div>

    <div class="ribbon">
      <svg class="abs" style="left:0;top:0" width="420" height="64" viewBox="0 0 420 64">
        <defs>
          <linearGradient id="ribbonFill" x1="0" y1="0" x2="1" y2="0">
            <stop offset="0" stop-color="#c5141a"/>
            <stop offset="0.5" stop-color="#e4321b"/>
            <stop offset="1" stop-color="#c5141a"/>
          </linearGradient>
        </defs>
        <polygon points="24,18 90,18 90,64 24,64 38,42" fill="var(--red)"/>
        <polygon points="330,18 396,18 382,42 396,64 330,64" fill="var(--red)"/>
        <polygon points="57,44 90,44 90,56" fill="var(--red-dark)"/>
        <polygon points="361,44 330,44 330,56" fill="var(--red-dark)"/>
        <rect x="57" y="0" width="304" height="45" fill="url(#ribbonFill)"/>
      </svg>
      <div class="ribbon__text">PARTNER WITH US &amp; EVERYBODY WINS!</div>
    </div>

    <div class="benefit" style="left:16px">
      <div class="benefit__icon">
        <svg width="22" height="22" viewBox="0 0 24 24" fill="none" stroke="#fff" stroke-width="1.6" stroke-linejoin="round" stroke-linecap="round">
          <path d="M12 2 L14.5 4 L17.7 3.7 L18.6 6.8 L21.4 8.4 L20.3 11.4 L21.4 14.4 L18.6 16 L17.7 19.1 L14.5 18.8 L12 21 L9.5 18.8 L6.3 19.1 L5.4 16 L2.6 14.4 L3.7 11.4 L2.6 8.4 L5.4 6.8 L6.3 3.7 L9.5 4 Z"/>
          <circle cx="12" cy="11.4" r="5"/>
          <path d="M9.8 11.4 L11.4 13 L14.3 10"/>
        </svg>
      </div>
      <div class="benefit__title">GUARANTEED<br>PAYOUT</div>
      <div class="benefit__body">Minimum <span class="hl">$500 or 10%</span><br>of Total Invoice Paid<br>Fast</div>
    </div>

    <div class="benefit" style="left:115px">
      <div class="benefit__icon">
        <svg width="20" height="20" viewBox="0 0 24 24" fill="none" stroke="#fff" stroke-width="1.6" stroke-linejoin="round" stroke-linecap="round">
          <rect x="8" y="4" width="13" height="17" rx="1.5"/>
          <rect x="10.5" y="6.5" width="8" height="3"/>
          <path d="M11 13h1M14.5 13h1M18 13h0.5M11 16h1M14.5 16h1M18 16h0.5M11 18.8h1M14.5 18.8h1"/>
          <path d="M5.5 3v1M5.5 10v1M7 5H4.8a1.3 1.3 0 0 0 0 2.6h1.4a1.3 1.3 0 0 1 0 2.6H4"/>
        </svg>
      </div>
      <div class="benefit__title">FREE<br>ESTIMATES</div>
      <div class="benefit__body"><span class="hl">Fast &amp; Free</span><br><span class="hl">Inspections</span> &amp; Written<br>Estimates</div>
    </div>

    <div class="benefit" style="left:214px">
      <div class="benefit__icon">
        <svg width="22" height="22" viewBox="0 0 24 24" fill="none" stroke="#fff" stroke-width="1.6" stroke-linejoin="round" stroke-linecap="round">
          <circle cx="13" cy="9" r="5"/>
          <path d="M13 6v6M14.6 7.2h-2.2a1 1 0 0 0 0 1.8h1.2a1 1 0 0 1 0 1.8h-2.2"/>
          <path d="M2.5 14.5h3l4 1.6h4a1.2 1.2 0 0 1 0 2.4H9.5"/>
          <path d="M5.5 20.5l3 .8 8-2.3 4.5-3.5a1.2 1.2 0 0 0-1.6-1.7l-3.4 2.3"/>
          <path d="M2.5 13.5v8"/>
        </svg>
      </div>
      <div class="benefit__title">AFFORDABLE<br>SOLUTIONS</div>
      <div class="benefit__body"><span class="hl">Lowest Out of</span><br><span class="hl">Pocket</span> Costs for Your<br>Customers</div>
    </div>

    <div class="benefit" style="left:312px">
      <div class="benefit__icon">
        <svg width="22" height="22" viewBox="0 0 24 24" fill="none" stroke="#fff" stroke-width="1.5" stroke-linejoin="round" stroke-linecap="round">
          <circle cx="12" cy="6.5" r="2.2"/>
          <circle cx="12" cy="6.5" r="4"/>
          <circle cx="5" cy="14" r="1.8"/><path d="M2 20c0-2 1.4-3.4 3-3.4s3 1.4 3 3.4"/>
          <circle cx="12" cy="14" r="1.8"/><path d="M9 20c0-2 1.4-3.4 3-3.4s3 1.4 3 3.4"/>
          <circle cx="19" cy="14" r="1.8"/><path d="M16 20c0-2 1.4-3.4 3-3.4s3 1.4 3 3.4"/>
        </svg>
      </div>
      <div class="benefit__title">INDUSTRY<br>LEADERS</div>
      <div class="benefit__body"><span class="hl">Licensed &amp; Certified</span><br><span class="hl">Experts</span> Provide 100%<br>Guarantee</div>
    </div>

    <div class="band-red"><span><span class="y">SEND</span> REFERRALS. <span class="y">GET</span> PAID. <span class="y">GROW</span> YOUR BUSINESS.</span></div>
    <div class="band-blue">
      <span class="band-blue__call">CALL, TEXT OR BOOK ONLINE</span>
      <span class="band-blue__phone">555-014-2796</span>
      <span class="band-blue__web">www.TallowRidgeBuilders.example</span>
    </div>
  </section>

  <!-- BACK SIDE -->
  <section class="flyer flyer--back">
    <div class="back-header">
      <div class="back-header__panel"></div>
      <div class="back-header__photo" role="img" aria-label="Photo of hundred-dollar bills with letter tiles spelling cash flow"></div>
      <div class="slogan slogan--small" style="top:28px">THE MORE YOU</div>
      <div class="slogan slogan--big" style="top:51px">REFER</div>
      <div class="slogan slogan--small" style="top:109px">THE MORE YOU</div>
      <div class="slogan slogan--big" style="top:133px;font-size:84px">EARN</div>
    </div>

    <div class="how"></div>
    <div class="how__title">HOW IT WORKS</div>

    <div class="step" style="left:9px">
      <div class="step__image step__image--city" role="img" aria-label="City skyline across the bay at dusk"></div>
      <div class="step__title">REFER<br>FLOOD, MOLD &amp;<br>CONSTRUCTION<br>JOBS</div>
      <div class="step__body" style="top:190px">It’s Simple to Refer<br>24/7: <span class="hl">Call, Text or<br>Book Online.</span></div>
    </div>

    <div class="step" style="left:146px">
      <div class="step__image step__image--home" role="img" aria-label="Inspector holding a work estimate clipboard in front of a house"></div>
      <div class="step__title">WE TAKE CARE<br>OF EVERYTHING</div>
      <div class="step__body" style="top:177px">We Schedule a <span class="hl">Free<br>Estimate.</span><br>If Approved, You Get<br>Paid.</div>
    </div>

    <div class="step" style="left:283px">
      <div class="step__image step__image--sign" role="img" aria-label="Yellow road sign reading get paid to share against a blue sky"></div>
      <div class="step__title">EVERYBODY<br>BENEFITS FROM<br>REFERRALS</div>
      <div class="step__body" style="top:184px">We Provide Expert<br>Quality Work for<br><span class="hl">Affordable Price.</span></div>
    </div>

    <div class="band-red"><span><span class="y">REFER:</span> FLOODS, REMODELS, RENOVATIONS &amp; REPAIRS</span></div>
    <div class="band-blue">
      <span class="band-blue__call">CALL, TEXT OR BOOK ONLINE</span>
      <span class="band-blue__phone">555-014-2796</span>
      <span class="band-blue__web">www.TallowRidgeBuilders.example</span>
    </div>
  </section>

</div>
</body>
</html>
```